Fitness competition business needs a card design

I need a professional business card design using my logo. The card will be horizontal with rounded edges.

Target Market(s)

Female fitness competitors

Industry/Entity Type

Fitness

Contact Information for Business Card

Rose-Lynn Darby
Owner
stagevarno.com
555.301.2187
info@stagevarno.com

Font styles to use
Serif

Colors

Designer to choose colors to be used in the design.

Requirements
Must have
• On the back please add the following:
• Figure
• Bikini
• Physique
• Fitness
Nice to have
• Looking for a very sleek design, contemporary and easy to read.
Should not have
• Should not be difficult to read or be too busy

```html
<!DOCTYPE html>
<html lang="en">
<head>
<meta charset="utf-8">
<title>Stage Varno – Business Card</title>
<link href="https://fonts.googleapis.com/css2?family=Tinos:wght@400;700&display=swap" rel="stylesheet">
<style>
  :root {
    --backdrop: #1e1f22;
    --card: #ffffff;
    --brand-red: #e0242b;
    --ink-grey: #4a4b4f;
    --text-dark: #2b2b2d;
    --photo-warm: #e9d3c4;
    --photo-blue: #6c8fd0;
    --photo-dark: #2a2a2e;
  }
  * { box-sizing: border-box; margin: 0; padding: 0; }
  html, body { width: 1200px; height: 800px; overflow: hidden; }
  body {
    background: var(--backdrop);
    font-family: "Tinos", "Times New Roman", serif;
    position: relative;
  }
  .card {
    position: absolute;
    width: 600px;
    height: 343px;
    background: var(--card);
    border-radius: 14px;
    overflow: hidden;
    box-shadow: 0 18px 40px rgba(0,0,0,0.45);
  }
  .card--back { left: 110px; top: 40px; }
  .card--front { left: 490px; top: 417px; }

  .brand {
    display: flex;
    align-items: center;
    gap: 12px;
    color: var(--brand-red);
    font-weight: 700;
    letter-spacing: 2px;
    white-space: nowrap;
  }
  .brand__dot {
    width: 24px; height: 24px;
    border-radius: 50%;
    background: var(--ink-grey);
    flex: none;
  }

  .back-lockup {
    position: absolute;
    left: 0; right: 0; top: 50%;
    transform: translateY(-50%);
    display: flex;
    flex-direction: column;
    align-items: center;
    gap: 18px;
  }
  .back-lockup .brand { font-size: 36px; }
  .divisions {
    display: flex;
    gap: 14px;
    list-style: none;
    color: var(--ink-grey);
    font-size: 15px;
    letter-spacing: 3px;
    text-transform: uppercase;
  }
  .divisions__item + .divisions__item::before {
    content: "";
    display: inline-block;
    width: 4px; height: 4px;
    border-radius: 50%;
    background: var(--brand-red);
    margin-right: 14px;
    vertical-align: middle;
  }

  .card--front .brand {
    position: absolute;
    left: 36px; top: 100px;
    font-size: 24px;
  }

  .photo {
    position: absolute;
    right: 0; top: 0;
    width: 290px; height: 343px;
    background: linear-gradient(160deg, var(--card) 0%, var(--photo-warm) 35%, var(--photo-blue) 65%, var(--photo-dark) 100%);
  }

  .contact { position: absolute; left: 36px; top: 196px; width: 260px; }
  .contact__name { color: var(--brand-red); font-size: 22px; line-height: 1.1; }
  .contact__role { color: var(--text-dark); font-size: 14px; margin-top: 2px; }
  .contact__rule { height: 1.5px; background: var(--brand-red); margin: 8px 0 10px; width: 240px; }
  .contact__list { list-style: none; }
  .contact__item {
    display: flex; align-items: center; gap: 9px;
    color: var(--text-dark); font-size: 14px; line-height: 23px;
  }
  .contact__icon { width: 16px; height: 16px; flex: none; }
</style>
</head>
<body>
  <section class="card card--back">
    <div class="back-lockup">
      <div class="brand"><span class="brand__dot"></span>STAGE VARNO</div>
      <ul class="divisions">
        <li class="divisions__item">Figure</li>
        <li class="divisions__item">Bikini</li>
        <li class="divisions__item">Physique</li>
        <li class="divisions__item">Fitness</li>
      </ul>
    </div>
  </section>

  <section class="card card--front">
    <div class="brand"><span class="brand__dot"></span>STAGE VARNO</div>

    <div class="photo" role="img" aria-label="Photo of two fitness athletes, a man in a blue shirt holding a clipboard and a woman lifting light dumbbells"></div>

    <div class="contact">
      <p class="contact__name">Rose-Lynn Darby</p>
      <p class="contact__role">Owner</p>
      <div class="contact__rule"></div>
      <ul class="contact__list">
        <li class="contact__item">
          <svg class="contact__icon" viewBox="0 0 16 16"><circle cx="8" cy="8" r="7.2" fill="none" stroke="var(--brand-red)" stroke-width="1.4"/><path d="M5 5.2c.4-.5 1-.5 1.3 0l.6 1c.2.4 0 .7-.3 1 .4.9 1 1.5 1.9 1.9.3-.3.6-.5 1-.3l1 .6c.5.3.5.9 0 1.3-1 .9-2.5.5-4-1s-1.9-3-1-4z" fill="var(--brand-red)"/></svg>
          555.301.2187
        </li>
        <li class="contact__item">
          <svg class="contact__icon" viewBox="0 0 16 16"><circle cx="8" cy="8" r="7.2" fill="none" stroke="var(--brand-red)" stroke-width="1.4"/><rect x="4" y="5.3" width="8" height="5.4" fill="var(--brand-red)"/><path d="M4 5.5l4 3 4-3" fill="none" stroke="#fff" stroke-width="0.9"/></svg>
          info@stagevarno.com
        </li>
        <li class="contact__item">
          <svg class="contact__icon" viewBox="0 0 16 16"><circle cx="8" cy="8" r="7.2" fill="none" stroke="var(--brand-red)" stroke-width="1.4"/><circle cx="8" cy="8" r="4" fill="none" stroke="var(--brand-red)" stroke-width="1"/><path d="M4 8h8M8 4c-1.6 2.2-1.6 5.8 0 8M8 4c1.6 2.2 1.6 5.8 0 8" fill="none" stroke="var(--brand-red)" stroke-width="0.9"/></svg>
          stagevarno.com
        </li>
      </ul>
    </div>
  </section>
</body>
</html>
```